Book Cover - The Velvet Lantern Almanac Collection

We are writing a book about the velvet lantern almanac collection, including Guerrilla Marketing. Advertising, Branding and PR.

We are looking for a fun and quirky cover, and are open to your ideas 💡
My website and social media are on www.TorvanPelica.co and posts are shared on Trelvano. Again we are open to ideas

```html
<!DOCTYPE html>
<html lang="en">
<head>
<meta charset="utf-8">
<title>The Velvet Lantern Almanac Collection — Book Cover</title>
<link href="https://fonts.googleapis.com/css2?family=Bebas+Neue&family=Poppins:wght@400&display=swap" rel="stylesheet">
<style>
  :root {
    --page: #ffffff;
    --street-dark: #2a2320;
    --street-warm: #6b4a2e;
    --sky: #7e9bb0;
    --frame: #1c1a19;
    --poster-red: #d92b27;
    --title-yellow: #f7e81c;
    --ink-black: #0c0c0c;
    --author-white: #ffffff;
    --grey-photo: #8c8c8c;
    --donut-pink: #f0a7b8;
  }
  html, body {
    margin: 0;
    width: 1200px;
    height: 1200px;
    overflow: hidden;
    background: var(--page);
  }
  .cover {
    position: absolute;
    left: 240px;
    top: 60px;
    width: 720px;
    height: 1080px;
    overflow: hidden;
  }
  .street-scene {
    position: absolute;
    inset: 0;
    background: linear-gradient(180deg, var(--sky) 0%, var(--street-warm) 45%, var(--street-dark) 100%);
  }
  .billboard-frame {
    position: absolute;
    left: 50px;
    top: 25px;
    width: 630px;
    height: 908px;
    background: var(--frame);
  }
  .poster {
    position: absolute;
    left: 67px;
    top: 48px;
    width: 571px;
    height: 842px;
    background: var(--poster-red);
    overflow: hidden;
  }
  .speech-ribbon {
    position: absolute;
    left: 300px;
    top: 40px;
    width: 280px;
    height: 270px;
    background: linear-gradient(160deg, #d8d8d8, var(--grey-photo));
    border-radius: 40% 20% 40% 30%;
  }
  .donut {
    position: absolute;
    left: 320px;
    top: 405px;
    width: 180px;
    height: 150px;
    border-radius: 50%;
    background: radial-gradient(circle, var(--donut-pink) 60%, #e58ea3 100%);
  }
  .businessman {
    position: absolute;
    left: 335px;
    top: 560px;
    width: 236px;
    height: 282px;
    background: linear-gradient(180deg, #5a5a5a, #1e1e1e);
  }
  .title {
    position: absolute;
    left: 14px;
    top: 40px;
    margin: 0;
    font-family: "Bebas Neue", "Oswald", sans-serif;
    font-weight: 400;
    font-size: 120px;
    line-height: 116px;
    color: var(--title-yellow);
    letter-spacing: 1px;
  }
  .title .line {
    display: block;
    height: 116px;
    white-space: nowrap;
  }
  .title .word {
    display: inline-block;
    vertical-align: top;
    height: 116px;
    line-height: 128px;
    padding: 0 6px;
    overflow: hidden;
  }
  .title .on-black { background: var(--ink-black); }
  .title .on-yellow { background: var(--title-yellow); color: var(--poster-red); }
  .title .band { padding-right: 400px; }
  .author {
    position: absolute;
    left: 387px;
    top: 1008px;
    margin: 0;
    font-family: "Poppins", sans-serif;
    font-size: 33px;
    color: var(--author-white);
  }
</style>
</head>
<body>
  <div class="cover">
    <div class="street-scene" role="img" aria-label="Evening city street with traffic light trails behind a billboard"></div>
    <div class="billboard-frame"></div>
    <div class="poster">
      <div class="speech-ribbon" role="img" aria-label="Collage of a mouth speaking a ribbon of blah-blah words into an ear"></div>
      <div class="donut" role="img" aria-label="Pink frosted donut with marshmallows circled by white lines"></div>
      <div class="businessman" role="img" aria-label="Black and white photo of a man in a suit holding a cup and saucer"></div>
      <h1 class="title">
        <span class="line"><span class="word">The</span></span>
        <span class="line"><span class="word on-black">Velvet</span></span>
        <span class="line"><span class="word on-black">Lan</span><span class="word on-yellow band">tern</span></span>
        <span class="line"><span class="word on-yellow">Almanac</span></span>
        <span class="line"><span class="word">Collec</span></span>
        <span class="line"><span class="word">tion</span></span>
      </h1>
    </div>
    <p class="author">Author Name</p>
  </div>
</body>
</html>
```